Healthcare IT company looking for business card design

We develop IT systems for healthcare that significantly reduces cost and improves quality.

We want a business card design that is professional and clean, and using the colors in our logo.

Target Market(s)

Doctors and decision makers in the healthcare industry

Industry/Entity Type

Healthcare

Contact Information for Business Card

It should include
Name and title, address, telephone

Tobias Vrenholt, CEO
+46 712 418257
tobias@kelvaro.se

Font styles to use
Serif

Colors
0355a3
ed282f

Requirements
Must have
• Clean design
• Professional feel
Nice to have
• N/A
Should not have
• N/A

```html
<!DOCTYPE html>
<html lang="en">
<head>
<meta charset="utf-8">
<title>Kelvaro — Business Card</title>
<link rel="stylesheet" href="https://fonts.googleapis.com/css2?family=EB+Garamond:wght@400;600&display=swap">
<style>
  :root {
    --brand-blue: #0355a3;
    --brand-red: #ed282f;
    --card-white: #f7f7f7;
    --card-edge: #e4e4e4;
    --ink: #2b2b2b;
    --ink-soft: #555;
    --backdrop: #2a2a2a;
  }
  * { margin: 0; padding: 0; box-sizing: border-box; }
  html, body {
    width: 1200px; height: 873px; overflow: hidden;
    background: var(--backdrop);
    font-family: "EB Garamond", Georgia, serif;
  }
  .canvas { position: relative; width: 1200px; height: 873px; }

  .card {
    position: absolute;
    width: 500px; height: 286px;
    background: linear-gradient(180deg, #ffffff 0%, var(--card-white) 60%, var(--card-edge) 100%);
    border-radius: 16px;
    overflow: hidden;
    box-shadow: 0 10px 30px rgba(0,0,0,.45);
  }
  .card--back { left: 60px; top: 150px; }
  .card--front { left: 640px; top: 437px; }

  /* Back side */
  .back-brand {
    position: absolute; left: 0; right: 0; top: 78px;
    text-align: center;
  }
  .back-brand .wordmark { font-size: 88px; }
  .back-url {
    position: absolute; left: 0; right: 0; top: 210px;
    text-align: center;
    font-size: 14px; letter-spacing: 4px; color: var(--ink-soft);
  }

  .wordmark {
    display: inline-flex; align-items: center; gap: 10px;
    font-weight: 600; color: var(--brand-blue); line-height: 1;
  }
  .wordmark .mark {
    display: inline-block; width: .22em; height: .22em;
    background: var(--brand-red);
  }

  /* Front side */
  .front-brand {
    position: absolute; left: 0; right: 0; top: 26px;
    text-align: center;
  }
  .front-brand .wordmark { font-size: 50px; }

  .contact-tab {
    position: absolute; right: 0; top: 82px;
    width: 48px; height: 110px;
    background: var(--brand-blue);
    border-radius: 12px 0 0 12px;
    display: flex; flex-direction: column; justify-content: space-around; align-items: center;
    padding: 8px 0;
  }
  .contact-tab svg { width: 20px; height: 20px; }

  .contact-list {
    position: absolute; right: 62px; top: 88px;
    list-style: none; text-align: right;
    font-size: 14px; color: var(--ink); line-height: 33px;
  }

  .person { position: absolute; left: 34px; top: 176px; }
  .person-name { font-size: 21px; font-weight: 600; color: var(--brand-blue); }
  .person-title { font-size: 13px; color: var(--ink-soft); margin-top: 2px; }

  .address-band {
    position: absolute; left: 0; right: 0; bottom: 0; height: 36px;
    background: var(--brand-blue);
    color: #fff; font-size: 15px; font-weight: 600;
    display: flex; align-items: center; justify-content: center;
    letter-spacing: .3px;
  }
  .accent-line {
    position: absolute; left: 0; right: 0; bottom: 36px; height: 3px;
    background: #fff;
  }
</style>
</head>
<body>
<main class="canvas">

  <section class="card card--back" aria-label="Card back">
    <div class="back-brand">
      <span class="wordmark">Kelvaro<span class="mark"></span></span>
    </div>
    <p class="back-url">www.kelvaro.se</p>
  </section>

  <section class="card card--front" aria-label="Card front">
    <div class="front-brand">
      <span class="wordmark">Kelvaro<span class="mark"></span></span>
    </div>

    <ul class="contact-list">
      <li>+46 712 418257</li>
      <li>+46 712 418257</li>
      <li>tobias@kelvaro.se</li>
    </ul>

    <div class="contact-tab">
      <svg viewBox="0 0 20 20" aria-label="Telephone" role="img">
        <path d="M3 8c0-2 3-4 7-4s7 2 7 4v1h-3V7.5c-1-.6-2.3-.9-4-.9s-3 .3-4 .9V9H3z" fill="none" stroke="#fff" stroke-width="1.4"/>
        <rect x="5" y="10" width="10" height="6" rx="1" fill="none" stroke="#fff" stroke-width="1.4"/>
      </svg>
      <svg viewBox="0 0 20 20" aria-label="Mobile" role="img">
        <rect x="6" y="2.5" width="8" height="15" rx="1.5" fill="none" stroke="#fff" stroke-width="1.4"/>
        <line x1="9" y1="15" x2="11" y2="15" stroke="#fff" stroke-width="1.4"/>
      </svg>
      <svg viewBox="0 0 20 20" aria-label="Email" role="img">
        <rect x="2.5" y="5" width="15" height="10" fill="none" stroke="#fff" stroke-width="1.4"/>
        <path d="M2.5 5l7.5 6 7.5-6" fill="none" stroke="#fff" stroke-width="1.4"/>
      </svg>
    </div>

    <div class="person">
      <p class="person-name">Tobias Vrenholt</p>
      <p class="person-title">CEO</p>
    </div>

    <div class="accent-line"></div>
    <div class="address-band">18 Linden Brook Road, 2nd Floor, Millbury, CT 06412</div>
  </section>

</main>
</body>
</html>
```